PLUMBING VAN LOGO/VINYL GRAPHIC CONTEST!

Our target audience is builders, contractors, designers, architects.

Upon discussion with some vinyl wrap companies we are now moving away from a full wrap and going for more simplistic lettering and logo design on the truck.
We are looking to apply vinyl graphics on top of a silver color Brannoc hauler 3400. (See attached picture for JUST CUT VINYL style design.

We would like to have our logo incorporated on to the sides of the truck (Must be shrunken down to fit the full logo - no cut off half images)

We would also like to have Custom homes, Additions, Renovations, as well as Commercial/Industrial incorporated onto the side of the van and also the back doors.

We would like to see variations of black and blue on top of the silver for a good color contrast. No light colours for the writing.

Hi Designers,

We are going to be changing the overall design stance of our project, we didn't find anything we particularly liked enough to use as a wrap for our trucks.

We would like to see some more simplistic ideas, and we have decided to keep the silver color of our trucks as a background. We will be going with vinyl graphics on top of the silver backdrop, instead of a full van wrap/color change.

With any new submissions, we would prefer to see our logo and our services listed on the truck, with different ideas for placement. Having a silver van color, we would prefer some darker bolder colors like black, blue, etc. and to avoid any light color schemes.

Important things to have on the design

Kestrow Plumbing Ltd
(logo)
(custom homes, additions, renovations)
(commercial/industrial)

Thank you to everybody who has/will submit designs.

• We are open to different fonts. We like the font in the logo but are open to other ideas.

• Kestrow Plumbing Ltd , Custom Homes, Additions, Renovations, Commercial/Residential
• Silver background on van, kestrow plumbing logo and kestrow plumbing ltd written on

```html
<!DOCTYPE html>
<html lang="en">
<head>
<meta charset="utf-8">
<title>Kestrow Plumbing Ltd — Van Sticker Design</title>
<link rel="stylesheet" href="https://fonts.googleapis.com/css2?family=Michroma&family=Exo+2:ital,wght@1,500&family=Roboto:wght@400&display=swap">
<style>
  :root {
    --brand-blue: #1b5aa6;
    --ink-dark: #2b2d31;
    --paper: #ffffff;
    --silver-light: #d6d7d9;
    --silver-mid: #b3b5b8;
    --silver-dark: #8f9195;
  }
  * { box-sizing: border-box; margin: 0; padding: 0; }
  html, body { width: 848px; height: 1200px; overflow: hidden; background: var(--paper); }
  .sheet { position: relative; width: 848px; height: 1200px; font-family: "Roboto", sans-serif; }

  .sheet-frame {
    position: absolute; left: 42px; top: 81px; width: 750px; height: 1063px;
    border: 2px solid var(--brand-blue);
  }
  .frame-gap { position: absolute; left: 669px; top: 77px; width: 104px; height: 10px; background: var(--paper); }
  .sheet-title {
    position: absolute; left: 93px; top: 104px; font-weight: 400;
    font-family: "Michroma", sans-serif; font-size: 16px; letter-spacing: 5.2px;
    color: var(--brand-blue); line-height: 1;
  }
  .corner-mark {
    position: absolute; left: 700px; top: 104px; width: 24px; height: 24px;
    border: 2px solid var(--brand-blue);
  }

  .van-area {
    position: absolute;
    background: linear-gradient(180deg, var(--silver-light) 0%, var(--silver-mid) 65%, var(--silver-dark) 100%);
  }

  .view-label {
    position: absolute; font-size: 17px; line-height: 1; color: var(--brand-blue); letter-spacing: 0.3px;
  }

  .decal { position: absolute; white-space: nowrap; line-height: 1; text-align: center; color: var(--brand-blue); }
  .wordmark { font-family: "Michroma", sans-serif; letter-spacing: 0.5px; }
  .wordmark-sub { font-family: "Michroma", sans-serif; }
  .services { font-size: 7px; letter-spacing: 0.45px; color: var(--ink-dark); }
  .services.on-glass { color: var(--brand-blue); }
  .sectors { font-family: "Exo 2", sans-serif; font-style: italic; font-weight: 500; font-size: 10.5px; text-align: left; }
  .sectors .dark { color: var(--ink-dark); }
</style>
</head>
<body>
<main class="sheet">
  <div class="sheet-frame"></div>
  <div class="frame-gap"></div>
  <h1 class="sheet-title">VAN STICKER DESIGN</h1>

  <div class="corner-mark"></div>
  <div class="decal wordmark" style="left:651px;top:137px;width:120px;font-size:13.5px;">KESTROW</div>
  <div class="decal wordmark-sub" style="left:651px;top:152px;width:120px;font-size:6.5px;letter-spacing:3.5px;">PLUMBING</div>

  <!-- Right side view -->
  <div class="van-area" style="left:112px;top:170px;width:622px;height:246px;border-radius:16px 60px 20px 16px;" role="img" aria-label="Photo of a silver panel van, right side"></div>
  <div class="decal wordmark" style="left:150px;top:212px;width:214px;font-size:24px;">KESTROW</div>
  <div class="decal wordmark-sub" style="left:180px;top:238px;width:150px;font-size:9px;letter-spacing:3px;">PLUMBING LTD</div>
  <div class="decal services" style="left:137px;top:277px;width:180px;">CUSTOM HOMES • ADDITIONS • RENOVATIONS</div>
  <div class="decal sectors" style="left:151px;top:297px;">INDUSTRIAL <span class="dark">COMMERCIAL</span></div>
  <div class="decal wordmark" style="left:316px;top:307px;width:142px;font-size:15px;">KESTROW</div>
  <div class="decal wordmark-sub" style="left:316px;top:323px;width:142px;font-size:7.5px;letter-spacing:3.5px;">PLUMBING</div>
  <div class="decal wordmark" style="left:520px;top:300px;width:100px;font-size:10px;">KESTROW</div>
  <div class="decal wordmark-sub" style="left:520px;top:311px;width:100px;font-size:4.5px;letter-spacing:1.5px;">PLUMBING LTD</div>
  <div class="view-label" style="left:399px;top:432px;">RIGHT</div>

  <!-- Left side view -->
  <div class="van-area" style="left:118px;top:476px;width:620px;height:244px;border-radius:60px 16px 16px 20px;" role="img" aria-label="Photo of a silver panel van, left side"></div>
  <div class="decal wordmark" style="left:492px;top:522px;width:214px;font-size:24px;">KESTROW</div>
  <div class="decal wordmark-sub" style="left:528px;top:548px;width:150px;font-size:9px;letter-spacing:3px;">PLUMBING LTD</div>
  <div class="decal services" style="left:534px;top:580px;width:180px;">CUSTOM HOMES • ADDITIONS • RENOVATIONS</div>
  <div class="decal sectors" style="left:549px;top:598px;">INDUSTRIAL <span class="dark">COMMERCIAL</span></div>
  <div class="decal wordmark" style="left:386px;top:610px;width:142px;font-size:15px;">KESTROW</div>
  <div class="decal wordmark-sub" style="left:386px;top:626px;width:142px;font-size:7.5px;letter-spacing:3.5px;">PLUMBING</div>
  <div class="decal wordmark" style="left:231px;top:597px;width:100px;font-size:10px;">KESTROW</div>
  <div class="decal wordmark-sub" style="left:231px;top:608px;width:100px;font-size:4.5px;letter-spacing:1.5px;">PLUMBING LTD</div>
  <div class="view-label" style="left:397px;top:738px;">LEFT</div>

  <!-- Front view -->
  <div class="van-area" style="left:112px;top:806px;width:286px;height:292px;border-radius:28px 28px 14px 14px;" role="img" aria-label="Photo of a silver panel van, front"></div>
  <div class="decal services on-glass" style="left:159px;top:826px;width:180px;">CUSTOM HOMES • ADDITIONS • RENOVATIONS</div>
  <div class="decal wordmark" style="left:190px;top:928px;width:122px;font-size:13.5px;">KESTROW</div>
  <div class="decal wordmark-sub" style="left:190px;top:942px;width:122px;font-size:6px;letter-spacing:2.5px;">PLUMBING LTD</div>
  <div class="view-label" style="left:215px;top:1111px;">FRONT</div>

  <!-- Rear view -->
  <div class="van-area" style="left:465px;top:797px;width:257px;height:298px;border-radius:20px 20px 12px 12px;" role="img" aria-label="Photo of a silver panel van, rear doors"></div>
  <div class="decal sectors" style="left:503px;top:836px;font-size:9px;">INDUSTRIAL</div>
  <div class="decal sectors" style="left:515px;top:848px;font-size:9px;"><span class="dark">COMMERCIAL</span></div>
  <div class="decal wordmark" style="left:516px;top:951px;width:150px;font-size:16.5px;">KESTROW</div>
  <div class="decal wordmark-sub" style="left:516px;top:968px;width:150px;font-size:8.5px;letter-spacing:3.5px;">PLUMBING</div>
  <div class="decal services" style="left:506px;top:986px;width:180px;">CUSTOM HOMES • ADDITIONS • RENOVATIONS</div>
  <div class="view-label" style="left:570px;top:1111px;">REAR</div>
</main>
</body>
</html>
```